Hop Grower Producer Card

A wisconsin based grower of high quality mid westrn grown Hops with the concept of growing and processing Hops into pellet form for sale to brewers of beer large and small .varieties are grown are Cascade ,Chinook and Centennial

Target Market(s)

Brew masters at micro brews and large breweries

Industry/Entity Type

Processing

Font styles to use
Decorative
Script

Requirements
Must have
• i would like the Hop varieties listed on the back of the card , with the statement Grower of High Quality Wisconsin Hops and the web site address
Nice to have
• german style font for the name Velmar's Bine Hollow

```html
<!DOCTYPE html>
<html lang="en">
<head>
<meta charset="utf-8">
<title>Velmar's Bine Hollow – Business Cards</title>
<link rel="stylesheet" href="https://fonts.googleapis.com/css2?family=Parisienne&family=Raleway:wght@500;700&display=swap">
<style>
  :root {
    --page: #ffffff;
    --sage-light: #eef0d4;
    --sage-mid: #dfe3b6;
    --leaf-green: #3e6b2d;
    --vine-green: #6c8c4f;
    --vine-green-faint: rgba(150, 168, 120, 0.35);
    --bark-brown: #4a1c14;
    --vine-brown: #6e4a3d;
    --vine-brown-faint: rgba(150, 120, 115, 0.22);
    --script: "Parisienne", cursive;
    --sans: "Raleway", sans-serif;
  }
  * { box-sizing: border-box; margin: 0; padding: 0; }
  html, body { width: 1200px; height: 718px; overflow: hidden; background: var(--page); }
  .sheet { position: relative; width: 1200px; height: 718px; }

  .card { position: absolute; overflow: hidden; }
  .card--front { top: 0; height: 352px; }
  .card--back { top: 358px; height: 360px; }
  .card--left { left: 0; width: 598px; }
  .card--right { left: 602px; width: 598px; }

  .card--sage {
    background: radial-gradient(ellipse at 60% 45%, var(--sage-light) 0%, var(--sage-mid) 100%);
    color: var(--leaf-green);
  }
  .card--plain { background: var(--page); color: var(--bark-brown); }

  .vine-art { position: absolute; left: 0; top: 0; height: 100%; }
  .card--front .vine-art { width: 190px; border-radius: 0 90px 90px 0; }
  .card--back .vine-art { width: 170px; border-radius: 0 80px 80px 0; }
  .card--sage.card--front .vine-art { background: linear-gradient(160deg, var(--vine-green) 0%, rgba(108,140,79,0.55) 60%, rgba(108,140,79,0.25) 100%); }
  .card--plain.card--front .vine-art { background: linear-gradient(160deg, var(--vine-brown) 0%, rgba(110,74,61,0.55) 60%, rgba(110,74,61,0.2) 100%); }
  .card--sage.card--back .vine-art { background: linear-gradient(160deg, var(--vine-green-faint), rgba(150,168,120,0.12)); }
  .card--plain.card--back .vine-art { background: linear-gradient(160deg, var(--vine-brown-faint), rgba(150,120,115,0.06)); }

  .owner {
    position: absolute; right: 30px; top: 28px; text-align: right;
    font-family: var(--script); font-size: 23px; line-height: 1.3;
  }
  .brand-name { font-family: var(--script); font-weight: 400; white-space: nowrap; }
  .front-block { position: absolute; right: 30px; top: 126px; text-align: right; }
  .front-block .brand-name { font-size: 42px; line-height: 1.1; }
  .tagline { font-family: var(--sans); font-weight: 700; }
  .front-block .tagline { font-size: 17.5px; margin-top: 10px; }

  .contact {
    position: absolute; right: 34px; top: 255px; text-align: right;
    font-family: var(--sans); font-weight: 500; font-size: 15px; line-height: 20px;
  }
  .contact strong { font-weight: 700; }

  .back-block {
    position: absolute; left: 0; right: 0; text-align: center;
  }
  .card--left .back-block { top: 80px; padding-left: 10px; }
  .card--right .back-block { top: 76px; padding-left: 0; }
  .back-block .brand-name { font-size: 52px; line-height: 1.1; }
  .back-block .tagline { font-size: 20px; margin-top: 24px; }
  .card--right .back-block .tagline { margin-top: 16px; }
  .varieties { font-family: var(--script); font-size: 30px; margin-top: 8px; }
  .website { font-family: var(--sans); font-weight: 700; font-size: 17.5px; margin-top: 8px; }

  .divider { display: block; margin: 6px auto 0; width: 342px; height: 12px; }
</style>
</head>
<body>
<main class="sheet">

  <section class="card card--front card--left card--sage">
    <div class="vine-art" role="img" aria-label="Climbing hop vine illustration with leaves and hop cones"></div>
    <p class="owner">Tomas Velmar<br>Manager/ Owner</p>
    <div class="front-block">
      <h1 class="brand-name">Velmar's Bine Hollow</h1>
      <p class="tagline">Grower of High Quality Wisconsin Hop</p>
    </div>
    <address class="contact" style="font-style:normal">
      2714 Millbrook Lane, Aldenford, WI 54390<br>
      Ph: 715-555-0142, Fax: 715-555-0187<br>
      Mail:<strong>binehollow14@mail.com</strong>
    </address>
  </section>

  <section class="card card--front card--right card--plain">
    <div class="vine-art" role="img" aria-label="Climbing hop vine illustration with leaves and hop cones"></div>
    <p class="owner">Tomas Velmar<br>Manager/ Owner</p>
    <div class="front-block">
      <h1 class="brand-name">Velmar's Bine Hollow</h1>
      <p class="tagline">Grower of High Quality Wisconsin Hop</p>
    </div>
    <address class="contact" style="font-style:normal">
      2714 Millbrook Lane, Aldenford, WI 54390<br>
      Ph: 715-555-0142, Fax: 715-555-0187<br>
      Mail:<strong>binehollow14@mail.com</strong>
    </address>
  </section>

  <section class="card card--back card--left card--sage">
    <div class="vine-art" role="img" aria-label="Faint hop vine illustration in the background"></div>
    <div class="back-block">
      <h2 class="brand-name">Velmar's Bine Hollow</h2>
      <p class="tagline">Grower of High Quality Wisconsin Hop</p>
      <p class="varieties">Cascade · Chinook · Centennial</p>
      <p class="website">www.binehollow14.com</p>
    </div>
  </section>

  <section class="card card--back card--right card--plain">
    <div class="vine-art" role="img" aria-label="Faint hop vine illustration in the background"></div>
    <div class="back-block">
      <h2 class="brand-name">Velmar's Bine Hollow</h2>
      <svg class="divider" viewBox="0 0 342 12" aria-hidden="true">
        <line x1="0" y1="6" x2="164" y2="6" stroke="currentColor" stroke-width="2"/>
        <line x1="178" y1="6" x2="342" y2="6" stroke="currentColor" stroke-width="2"/>
        <circle cx="171" cy="6" r="4" fill="none" stroke="currentColor" stroke-width="1.5"/>
      </svg>
      <p class="tagline">Grower of High Quality Wisconsin Hop</p>
      <p class="varieties">Cascade · Chinook · Centennial</p>
      <p class="website">www.binehollow14.com</p>
    </div>
  </section>

</main>
</body>
</html>
```